Aunt Rolina's Bakery

I am about to create a luxury boutique that specializes in cake baking and cupcake
and ready for parties and special events and order delivery
the logo has already made

Industry/Entity Type

Boutique

Contact Information for Business Card

Email:auntrolinasbakery@maplecrumbmail.com
Instagram: aunt_rolina_bakery
Twitter: xxxxxxx
WhatsApp: xxxxxxx

Requirements
Must have
• luxury design

```html
<!DOCTYPE html>
<html lang="en">
<head>
<meta charset="utf-8">
<title>Aunt Rolina's Bakery — Business Card</title>
<link href="https://fonts.googleapis.com/css2?family=Arimo:wght@400;700&display=swap" rel="stylesheet">
<style>
  :root {
    --backdrop: #3b322e;
    --card: #1c1c1d;
    --card-edge: #2a2a2b;
    --rose: #d99aae;
    --rose-deep: #a9707f;
    --ink-light: #f2f2f2;
    --line: #8e8e8e;
    --ornament-tone: rgba(185, 185, 185, 0.28);
  }
  * { box-sizing: border-box; margin: 0; padding: 0; }
  html, body {
    width: 1200px; height: 787px; overflow: hidden;
    background: var(--backdrop);
    font-family: "Arimo", Arial, sans-serif;
  }
  .stage {
    position: relative; width: 1200px; height: 787px;
    display: flex; align-items: center; justify-content: center; gap: 30px;
  }
  .card {
    position: relative; width: 560px; height: 320px;
    background: var(--card);
    border: 1px solid var(--card-edge);
    border-radius: 4px;
    overflow: hidden;
  }

  /* Back side */
  .card-back .brand-seal {
    position: absolute; left: 150px; top: 50px;
    width: 150px; height: 150px; border-radius: 50%;
    background: var(--rose-deep);
    border: 6px solid #3c3c3e;
    display: flex; align-items: center; justify-content: center;
    text-align: center;
  }
  .card-back .brand-seal span {
    color: var(--ink-light); font-size: 17px; font-weight: 700;
    line-height: 1.25; padding: 0 14px;
  }
  .card-back .website {
    position: absolute; left: 92px; top: 226px;
    color: var(--ink-light); font-size: 12px; letter-spacing: 3px;
  }

  /* Front side */
  .card-front .frame {
    position: absolute; inset: 18px;
    border: 1.5px solid var(--line);
  }
  .card-front .corner {
    position: absolute; width: 40px; height: 40px;
  }
  .corner.tl { left: 6px; top: 6px;
    background: radial-gradient(circle at 12px 12px, var(--ornament-tone), transparent 70%); }
  .corner.tr { right: 6px; top: 6px;
    background: radial-gradient(circle at 28px 12px, var(--ornament-tone), transparent 70%); }
  .corner.bl { left: 6px; bottom: 6px;
    background: radial-gradient(circle at 12px 28px, var(--ornament-tone), transparent 70%); }
  .corner.br { right: 6px; bottom: 6px;
    background: radial-gradient(circle at 28px 28px, var(--ornament-tone), transparent 70%); }

  .brand {
    position: absolute; left: 34px; top: 104px; width: 190px;
    display: flex; flex-direction: column; align-items: center; gap: 10px;
  }
  .brand-dot {
    width: 36px; height: 36px; border-radius: 50%;
    background: var(--rose);
  }
  .brand-name {
    color: var(--rose); font-size: 21px; font-weight: 700;
    text-align: center; line-height: 1.2;
  }
  .divider {
    position: absolute; left: 240px; top: 90px;
    width: 1px; height: 120px; background: var(--line);
  }
  .details { position: absolute; left: 258px; top: 90px; }
  .person-name { color: var(--rose); font-size: 18px; font-weight: 700; }
  .person-role { color: var(--ink-light); font-size: 13px; margin-top: 3px; }
  .contact-list { list-style: none; margin-top: 12px; }
  .contact-list li {
    display: flex; align-items: center; gap: 8px;
    color: var(--ink-light); font-size: 11px; line-height: 19px;
    white-space: nowrap;
  }
  .contact-list svg { width: 13px; height: 13px; flex: none; }
  .icon-dot {
    width: 11px; height: 11px; margin: 0 1px;
    border-radius: 50%; background: var(--rose); flex: none;
  }
</style>
</head>
<body>
<main class="stage">

  <section class="card card-back" aria-label="Business card back">
    <div class="brand-seal"><span>Aunt Rolina's Bakery</span></div>
    <p class="website">www.rolinabakes.com</p>
  </section>

  <section class="card card-front" aria-label="Business card front">
    <div class="frame"></div>
    <div class="corner tl" role="img" aria-label="Silver scroll flourish corner ornament"></div>
    <div class="corner tr" role="img" aria-label="Silver scroll flourish corner ornament"></div>
    <div class="corner bl" role="img" aria-label="Silver scroll flourish corner ornament"></div>
    <div class="corner br" role="img" aria-label="Silver scroll flourish corner ornament"></div>

    <div class="brand">
      <div class="brand-dot"></div>
      <p class="brand-name">Aunt Rolina's Bakery</p>
    </div>

    <div class="divider"></div>

    <div class="details">
      <h1 class="person-name">Maya Terrence</h1>
      <p class="person-role">President</p>
      <ul class="contact-list">
        <li>
          <svg viewBox="0 0 16 16" aria-hidden="true"><path fill="#d99aae" d="M3.5 1.5l2.5 0 1 3.5-1.6 1.2c.8 1.8 2.2 3.2 4 4L10.6 8.6l3.4 1v2.6c0 .9-.8 1.6-1.7 1.5C6.7 13.2 2.8 9.3 2.3 3.7 2.2 2.7 2.7 1.5 3.5 1.5z"/></svg>
          555 0147 2286
        </li>
        <li>
          <svg viewBox="0 0 16 16" aria-hidden="true"><rect x="1" y="3" width="14" height="10" rx="1" fill="#d99aae"/><path d="M1.5 3.6L8 9l6.5-5.4" fill="none" stroke="#1c1c1d" stroke-width="1.3"/></svg>
          auntrolinasbakery@maplecrumbmail.com
        </li>
        <li><span class="icon-dot"></span>aunt_rolina_bakery</li>
        <li><span class="icon-dot"></span>auntrolinasbakery</li>
        <li><span class="icon-dot"></span>auntrolinasbakery</li>
      </ul>
    </div>
  </section>

</main>
</body>
</html>
```